Stationary - Based On Previous Design

Basic stationary with a header and footer

Target Market(s)

Friends, Colleagues, More friendly than professional

Industry/Entity Type

legal/personal

Colors
00AB8E
00BBA5
67D7C9
C6EFE9
E9F9F6

Requirements
Must have
• Green & White
Nice to have
• I like the "P" on the business card and was thinking that would be for both P's in "PembaPixo"
Should not have
• other colors

```html
<!DOCTYPE html>
<html lang="en">
<head>
<meta charset="utf-8">
<title>PembaPixo Stationery</title>
<link rel="stylesheet" href="https://fonts.googleapis.com/css2?family=Open+Sans:wght@400&family=Roboto:wght@400;500&display=swap">
<style>
  :root {
    --green: #2d4f31;
    --paper: #eeeeee;
    --backdrop: #e4e4e4;
    --ink: #3c3c3c;
    --faint: #dcdedb;
    --white: #f2f2f2;
  }
  html, body { margin: 0; padding: 0; overflow: hidden; }
  body { width: 1200px; height: 795px; background: var(--backdrop); position: relative; font-family: "Roboto", sans-serif; }
  .sheet { position: absolute; box-shadow: 0 1px 4px rgba(0,0,0,.12); }
  .brand { font-family: "Roboto", sans-serif; font-weight: 500; color: var(--green); display: flex; align-items: center; gap: 5px; white-space: nowrap; }
  .brand .dot { border-radius: 50%; background: currentColor; flex: none; }

  /* Letterhead */
  .letterhead { left: 292px; top: 99px; width: 294px; height: 415px; background: var(--paper); }
  .letterhead .brand { position: absolute; top: 23px; left: 0; right: 0; justify-content: center; font-size: 17px; }
  .letterhead .brand .dot { width: 9px; height: 9px; }
  .letter { position: absolute; left: 27px; top: 100px; width: 240px; font-family: "Open Sans", sans-serif; font-size: 5.4px; line-height: 8px; color: var(--ink); }
  .letter p { margin: 0 0 8px; text-align: justify; }
  .signature { width: 36px; height: 30px; background: var(--faint); margin-top: 8px; border-radius: 3px; }
  .letter-footer { position: absolute; left: 0; right: 0; top: 379px; text-align: center; font-size: 6.6px; line-height: 10px; color: var(--ink); }
  .icon { display: inline-block; vertical-align: -1px; }

  /* Folder */
  .folder { left: 637px; top: 80px; width: 347px; height: 437px; background: var(--green); }
  .folder .spine { position: absolute; left: 16px; top: 0; bottom: 0; width: 1px; background: rgba(0,0,0,.18); }
  .folder .emblem { position: absolute; left: 74px; top: 105px; width: 200px; height: 200px; border-radius: 50%; background: #e9e9e9; }
  .folder .web { position: absolute; left: 0; right: 0; top: 400px; text-align: center; color: var(--white); font-size: 10.5px; letter-spacing: .2px; }

  /* Business cards */
  .card { left: 187px; width: 132px; height: 75px; }
  .card-front { top: 551px; background: var(--paper); text-align: center; }
  .card-front .brand { justify-content: center; font-size: 11px; margin-top: 9px; }
  .card-front .brand .dot { width: 6px; height: 6px; }
  .card-front .name { margin-top: 6px; font-size: 4.6px; font-weight: 500; color: var(--green); text-transform: uppercase; }
  .card-front .role { font-size: 4px; color: var(--ink); margin-top: 1px; }
  .card-front .contact { font-size: 3.8px; color: var(--ink); margin-top: 5px; line-height: 6px; }
  .card-back { top: 647px; background: var(--green); display: flex; align-items: center; justify-content: center; }
  .card-back .brand { color: var(--white); font-size: 14px; }
  .card-back .brand .dot { width: 7px; height: 7px; }

  /* Window envelope */
  .envelope-front { left: 353px; top: 561px; width: 329px; height: 157px; background: var(--paper); overflow: hidden; }
  .envelope-front .brand { position: absolute; left: 21px; top: 21px; font-size: 13.5px; }
  .envelope-front .brand .dot { width: 7px; height: 7px; }
  .envelope-front .backdrop-mark { position: absolute; left: 198px; top: 14px; width: 132px; height: 132px; border-radius: 50%; background: var(--faint); }
  .envelope-front .address { position: absolute; left: 22px; top: 103px; font-size: 7px; line-height: 8.6px; color: var(--ink); }

  /* Envelope back */
  .envelope-back { left: 714px; top: 561px; width: 328px; height: 157px; background: var(--paper); overflow: hidden; }
  .envelope-back .flap { position: absolute; left: 0; top: 0; width: 328px; height: 56px; }
  .envelope-back .flap-mark { position: absolute; left: 151px; top: 14px; width: 26px; height: 26px; border-radius: 50%; background: var(--white); }
</style>
</head>
<body>

  <article class="sheet letterhead">
    <div class="brand"><span class="dot"></span>PembaPixo</div>
    <div class="letter">
      <p>Dear customer,</p>
      <p>Lorem ipsum dolor sit amet, consectetur adipisicing elit, sed do eiusmod tempor incididunt ut labore et dolore magna aliqua. Ut enim ad minim veniam, quis nostrud exercitation ullamco laboris nisi ut aliquip ex ea commodo consequat. Duis aute irure dolor in reprehenderit in voluptate velit esse cillum dolore eu fugiat nulla pariatur. Excepteur sint occaecat cupidatat non proident, sunt in culpa qui officia deserunt mollit anim id est laborum.</p>
      <p>Lorem ipsum dolor sit amet, consectetur adipisicing elit, sed do eiusmod tempor incididunt ut labore et dolore magna aliqua. Ut enim ad minim veniam, quis nostrud exercitation ullamco laboris nisi ut aliquip ex ea commodo consequat. Duis aute irure dolor in reprehenderit in voluptate velit esse cillum dolore eu fugiat nulla pariatur. Excepteur sint occaecat cupidatat non proident, sunt in culpa qui officia deserunt mollit anim id est laborum.</p>
      <p>Lorem ipsum dolor sit amet, consectetur adipisicing elit, sed do eiusmod tempor incididunt ut labore et dolore magna aliqua. Ut enim ad minim veniam, quis nostrud exercitation ullamco laboris nisi ut aliquip ex ea commodo consequat. Duis aute irure dolor in reprehenderit in voluptate velit esse cillum dolore eu fugiat nulla pariatur. Excepteur sint occaecat cupidatat non proident, sunt in culpa qui officia deserunt mollit anim id est laborum.</p>
      <p>Lorem ipsum dolor sit amet, consectetur adipisicing elit, sed do eiusmod tempor incididunt ut labore et dolore magna aliqua. Ut enim ad minim veniam, quis nostrud exercitation ullamco laboris nisi ut aliquip ex ea commodo consequat. Duis aute irure dolor in reprehenderit.</p>
      <p>Yours Sincerely,</p>
      <div class="signature" role="img" aria-label="Handwritten signature"></div>
    </div>
    <div class="letter-footer">
      418 N Larkin Ave Riverton, IL 60632<br>
      <svg class="icon" width="7" height="6" viewBox="0 0 7 6" aria-hidden="true"><path d="M0 2 Q3.5 -0.5 7 2 L6 3 L4.6 2.2 L2.4 2.2 L1 3 Z M1.5 3.2 H5.5 L6.3 6 H0.7 Z" fill="var(--green)"/></svg> 555.014.2290&nbsp;&nbsp;
      <svg class="icon" width="7" height="6" viewBox="0 0 7 6" aria-hidden="true"><path d="M0 2.2 L3.5 0 L7 2.2 V6 H0 Z" fill="var(--green)"/><path d="M0.6 2.4 L3.5 4.2 L6.4 2.4" stroke="#fff" stroke-width=".7" fill="none"/></svg> treyhill@reyhillfirm.com
    </div>
  </article>

  <section class="sheet folder">
    <div class="spine"></div>
    <div class="emblem"></div>
    <div class="web">www.reyhillfirm.com</div>
  </section>

  <article class="sheet card card-front">
    <div class="brand"><span class="dot"></span>PembaPixo</div>
    <div class="name">Tomas Reyhill</div>
    <div class="role">President • Chief Legal Counsel</div>
    <div class="contact">418 N Larkin Ave Riverton, IL 60632<br>555.014.2290 &nbsp;treyhill@reyhillfirm.com</div>
  </article>

  <article class="sheet card card-back">
    <div class="brand"><span class="dot"></span>PembaPixo</div>
  </article>

  <article class="sheet envelope-front">
    <div class="backdrop-mark"></div>
    <div class="brand"><span class="dot"></span>PembaPixo</div>
    <div class="address">
      418 N Larkin Ave<br>
      Riverton, IL 60632<br>
      <svg class="icon" width="7" height="6" viewBox="0 0 7 6" aria-hidden="true"><path d="M0 2 Q3.5 -0.5 7 2 L6 3 L4.6 2.2 L2.4 2.2 L1 3 Z M1.5 3.2 H5.5 L6.3 6 H0.7 Z" fill="var(--green)"/></svg> 555.014.2290<br>
      <svg class="icon" width="7" height="6" viewBox="0 0 7 6" aria-hidden="true"><path d="M0 2.2 L3.5 0 L7 2.2 V6 H0 Z" fill="var(--green)"/><path d="M0.6 2.4 L3.5 4.2 L6.4 2.4" stroke="#fff" stroke-width=".7" fill="none"/></svg> treyhill@reyhillfirm.com
    </div>
  </article>

  <article class="sheet envelope-back">
    <svg class="flap" viewBox="0 0 328 56" aria-hidden="true"><path d="M0 0 H328 L323 50 Q322 55 316 55 H12 Q7 55 6 50 Z" fill="var(--green)"/></svg>
    <div class="flap-mark"></div>
  </article>

</body>
</html>
```